Medical Billing - Professional Marketing Flier

We are needing help designing a clean and professional looking easy to read marketing flier for a medical billing practice. The text needs to be large enough to print. We are looking for a 5.5 x 8.5 design that we can edit the text as needed. I have included our logo and what we initially want it to say. Please keep in mind, we also want our logo and contact details on the flier. Let me know if you have any questions.

```html
<!DOCTYPE html>
<html lang="en">
<head>
<meta charset="utf-8">
<title>Lyra Medical Billing – Flier</title>
<link rel="stylesheet" href="https://fonts.googleapis.com/css2?family=Roboto+Slab:wght@700&family=Ubuntu:wght@400;500;700&display=swap">
<style>
:root{
  --bg:#96979b;
  --blue:#3d5cae;
  --pink:#c85ea8;
  --purple:#7f5ca8;
  --violet:#9a5fb0;
  --ink:#6b6b70;
  --black:#0a0a0c;
  --white:#ffffff;
}
*{box-sizing:border-box;margin:0;padding:0}
html,body{width:1154px;height:1200px;overflow:hidden;background:var(--bg)}
.canvas{position:relative;width:1154px;height:1200px;overflow:hidden}
.flier{
  position:absolute;left:207px;top:28px;width:982px;height:1518px;
  transform:scale(.7536);transform-origin:0 0;
  background:var(--white);font-family:"Ubuntu",sans-serif;overflow:hidden;
}
.hero{position:absolute;left:0;top:0;width:982px;height:460px}
.brand{position:absolute;left:30px;top:140px;width:370px;text-align:center;color:var(--purple)}
.brand-name{font-size:92px;font-weight:400;letter-spacing:4px;line-height:1;display:flex;align-items:center;justify-content:center;gap:16px}
.brand-dot{width:40px;height:40px;border-radius:50%;background:var(--purple)}
.brand-sub{font-size:22px;font-weight:400;letter-spacing:6px;margin-top:8px;border-top:2px solid var(--purple);padding-top:6px}
.tagline{position:absolute;left:700px;top:342px;width:260px;text-align:center;color:var(--white);font-weight:700;font-size:29px;line-height:33px}
.services{position:absolute;left:0;top:480px;width:982px;height:120px}
.heading{position:absolute;top:612px;font-family:"Roboto Slab",serif;font-weight:700;font-size:28px;color:var(--blue);text-align:center}
.h-billing{left:0;width:350px}
.h-aging{left:350px;width:315px}
.h-cred{left:665px;width:317px}
.columns{position:absolute;left:0;top:658px;width:982px;height:524px;
  background:linear-gradient(90deg,#7a5fab 0%,#9b60af 50%,#d062a8 100%)}
.col{position:absolute;top:0;height:524px;padding-top:16px;color:var(--white);font-size:23.5px;line-height:26.8px;text-align:justify;text-align-last:center}
.col-billing{left:33px;width:285px}
.col-aging{left:372px;width:272px}
.col-cred{left:682px;width:270px}
.gutter{position:absolute;top:0;width:5px;height:524px;background:var(--white)}
.intro{position:absolute;left:33px;top:1208px;width:919px;color:var(--ink);font-size:23.5px;line-height:26.8px;text-align:justify}
.intro b{font-weight:700}
.footer{position:absolute;left:0;top:1363px;width:982px;height:155px;background:var(--black);color:var(--white)}
.footer-brand{position:absolute;left:34px;top:50px;width:170px;text-align:center;color:var(--purple)}
.footer-brand .brand-name{font-size:44px;letter-spacing:2px;gap:8px}
.footer-brand .brand-dot{width:18px;height:18px}
.footer-brand .brand-sub{font-size:10px;letter-spacing:2px;margin-top:3px;border-top-width:1px;padding-top:3px}
.email{position:absolute;left:275px;top:43px;width:395px;height:38px;border:2px solid var(--pink);border-radius:19px;display:flex;align-items:center;gap:14px;padding-left:16px;font-weight:700;font-size:21px}
.phone{position:absolute;left:292px;top:90px;display:flex;align-items:center;gap:16px;font-weight:700;font-size:31px;letter-spacing:1px}
.divider{position:absolute;left:712px;top:22px;width:3px;height:117px;background:var(--pink)}
.address{position:absolute;left:760px;top:42px;display:flex;gap:14px;font-weight:500;font-size:22px;line-height:27px}
</style>
</head>
<body>
<div class="canvas">
  <article class="flier">
    <svg class="hero" viewBox="0 0 982 460" aria-hidden="false">
      <defs>
        <linearGradient id="photoTone" x1="0" y1="0" x2="1" y2="1">
          <stop offset="0" stop-color="#b9bcc4"/>
          <stop offset=".55" stop-color="#d8cfc8"/>
          <stop offset="1" stop-color="#8d8f98"/>
        </linearGradient>
        <linearGradient id="swoosh" x1="0" y1="1" x2="1" y2="0">
          <stop offset="0" stop-color="#7f5ca8"/>
          <stop offset="1" stop-color="#c85ea8"/>
        </linearGradient>
      </defs>
      <rect role="img" aria-label="Photo of a smiling billing specialist at a desk with spreadsheets on computer monitors" x="440" y="0" width="542" height="425" fill="url(#photoTone)"/>
      <path d="M0,0 H585 C565,270 360,450 0,432 Z" fill="var(--blue)"/>
      <path d="M0,0 H560 C545,265 350,438 0,418 Z" fill="url(#swoosh)"/>
      <path d="M0,0 H536 C520,255 340,425 0,403 Z" fill="var(--white)"/>
      <path d="M626,460 C633,372 700,330 790,330 H982 V460 Z" fill="var(--pink)"/>
      <path d="M638,460 C648,382 710,338 800,330 H982 V460 Z" fill="var(--blue)"/>
    </svg>
    <div class="brand">
      <div class="brand-name"><span class="brand-dot"></span>LYRA</div>
      <div class="brand-sub">MEDICAL BILLING</div>
    </div>
    <p class="tagline">Medical billing tailored to your practices needs</p>

    <svg class="services" viewBox="0 0 982 120">
      <defs>
        <linearGradient id="badge" x1="0" y1="0" x2="1" y2="0">
          <stop offset="0" stop-color="#7f5ca8"/>
          <stop offset="1" stop-color="#d062a8"/>
        </linearGradient>
      </defs>
      <g fill="var(--blue)">
        <rect x="0" y="58" width="110" height="7"/>
        <rect x="240" y="58" width="202" height="7"/>
        <rect x="573" y="58" width="180" height="7"/>
        <rect x="882" y="58" width="100" height="7"/>
      </g>
      <g fill="url(#badge)">
        <circle cx="176" cy="61" r="57"/>
        <circle cx="508" cy="61" r="57"/>
        <circle cx="817" cy="61" r="57"/>
      </g>
      <g fill="none" stroke="var(--white)" stroke-width="5" stroke-linecap="round" stroke-linejoin="round">
        <rect x="148" y="27" width="56" height="72" rx="6"/>
        <rect x="164" y="20" width="24" height="14" rx="3"/>
        <circle cx="176" cy="66" r="14"/>
        <path d="M176,58 V74 M168,66 H184"/>
        <path d="M508,52 C500,36 478,42 484,58 C488,68 508,80 508,80 C508,80 528,68 532,58 C538,42 516,36 508,52 Z"/>
        <path d="M508,55 V69 M501,62 H515"/>
        <path d="M470,68 V86 L486,102 M546,68 V86 L530,102"/>
        <path d="M790,30 H836 L846,40 V94 H790 Z"/>
        <circle cx="808" cy="52" r="11"/>
        <path d="M808,46 V58 M802,52 H814 M798,74 H822 M798,84 H816"/>
        <path d="M838,70 L852,76 V86 C852,94 844,98 838,100 C832,98 824,94 824,86 V76 Z"/>
        <path d="M832,85 L837,90 L845,81"/>
      </g>
    </svg>

    <h2 class="heading h-billing">MEDICAL BILLING</h2>
    <h2 class="heading h-aging">AGING</h2>
    <h2 class="heading h-cred">CREDENTIALING</h2>

    <section class="columns">
      <p class="col col-billing">Would you prefer to spend time focusing on your clients and running your practice rather than trying to stay up to speed with the constantly changing medical billing rules and regulations? Let us help you by managing your medical billing and dealing with the insurance companies on your behalf! We work with you to tailor the entire medical billing process to suit your practices needs while making it as smooth and painless as possible.</p>
      <div class="gutter" style="left:345px"></div>
      <p class="col col-aging">Are you leaving money on the table? Are you able to do the follow-through needed to keep your aging in check and more money flowing into your practice? Are you uncertain about how to get insurance to pay on claims that should be covered but for some reason they decided not to? We can clean up your aging, reduce the amount of time it takes for claims to pay out, and we can keep your aging to a minimum.</p>
      <div class="gutter" style="left:660px"></div>
      <p class="col col-cred">Are you wanting to get contracted with insurance companies but aren’t sure how to go about it? Are you wanting to expand your client base by having the option to bill insurance? Let us take the confusion out of what can seem like a daunting task! We can get you and your practitioners contracted with the insurance companies of your choice and help you navigate through the process every step of the way!</p>
    </section>

    <p class="intro">If any of these processes are something you would like our help with or to consult with us on, please <b>email us</b> or give us <b>a call!</b> We specialize in billing and contracting for Nutritionists and Dietitians. We would love to help you expand your business and take the pain and frustration out of billing so you can focus on your clients.</p>

    <footer class="footer">
      <div class="footer-brand">
        <div class="brand-name"><span class="brand-dot"></span>LYRA</div>
        <div class="brand-sub">MEDICAL BILLING</div>
      </div>
      <div class="email">
        <svg width="28" height="20" viewBox="0 0 28 20" aria-hidden="true"><rect x="1.5" y="1.5" width="25" height="17" rx="2" fill="none" stroke="var(--pink)" stroke-width="3"/><path d="M2,3 L14,12 L26,3" fill="none" stroke="var(--pink)" stroke-width="3"/></svg>
        admin@lyramedicalbilling.com
      </div>
      <div class="phone">
        <svg width="26" height="26" viewBox="0 0 24 24" aria-hidden="true"><path fill="var(--pink)" d="M20 15.5c-1.2 0-2.4-.2-3.6-.6a1 1 0 0 0-1 .25l-2.2 2.2a15 15 0 0 1-6.6-6.6l2.2-2.2a1 1 0 0 0 .25-1A11 11 0 0 1 8.5 4a1 1 0 0 0-1-1H4a1 1 0 0 0-1 1 17 17 0 0 0 17 17 1 1 0 0 0 1-1v-3.5a1 1 0 0 0-1-1z"/></svg>
        555-014-2290
      </div>
      <div class="divider"></div>
      <div class="address">
        <svg width="22" height="30" viewBox="0 0 22 30" aria-hidden="true"><path fill="var(--pink)" d="M11 0C5 0 0 4.8 0 10.8 0 18 11 30 11 30s11-12 11-19.2C22 4.8 17 0 11 0zm0 15a4.5 4.5 0 1 1 0-9 4.5 4.5 0 0 1 0 9z"/></svg>
        <span>PO Box 410<br>Cedar Falls,<br>WA 98000</span>
      </div>
    </footer>
  </article>
</div>
</body>
</html>
```